Football (soccer) board game app design

Hi,

We are a start up looking for a gameplay design for an app. It is a football trivia app that consists of four main screens; login/register, main navigation, gameplay, question.

OVERALL:
We want our app to be kept in a dark theme. Black or very dark gray is preferable, with a couple of nice colors to give it a stylish touch. We like flat designs, but are open for ideas within the general structure design. The logo can be used in the app, but feel free to improve it you feel you can. In the attached material we have tried to outline some of our ideas and other designs friends have helped us make.

LOGIN/REGISTER:
We want a simple login. Email, password, Chatterly login and the possibility to register a new user. Live search check whether the email is valid and free, and there is also live validation of passwords. If this could be incorporated in the design it would be nice.

MAIN NAVIGATION:
In the main navigation screen we want it to be divided into tabs. A home, my games, my categories and a ranking tab. In the top bar it should be possible to search for categories as well as there should be a button to go to settings.

The Home tab
In the home tab we want a "Quick Play" button, and a list of featured categories. A category can be unlocked or locked, which should be illustrated somehow. When a category is tapped it should divide the block into a left and right tap area, where the user can choose to "Beat to unlock" or "Buy to unlock" if locked and "Practice" or "Challenge Friend" if already unlocked.

The My Games tab
In the my games tab, the current games should be divided into three lists. First "your turn", then "opponents turn" and finally "finished games".

The My Categories tab
This tab should include a list of categories, which the user have bought, but as of design it is fairly similar to the blocks in home tab. So not much different here.

The Ranking tab
Ranking should show a set of leaderboards; Today, This Week, This Month, etc. The row in a leaderboard should have teamname and a win percentage.

GAMEPLAY:
The gameplay is inspired by an old football (soccer) board game from the 1950's, and our gameplay consists of three core elements; a football (soccer) pitch, 11 players and a scoreboard.

The football (soccer) pitch
What we need is a pitch seen from behind the goal line. The important issue here, is the perspective, as we want 11 players on the field formed as a 4-3-3 formation, being 1 goalkeeper, 4 defenders, 3 midfielder and 3 strikers. They should all be touchable without overlap. In the other end we want a goal that should be touchable as well. The goal in the nearest end do not have to be visible. Due to the perspective of the field and the fact that players and goal should be touchable, of course give you the opportunity to play around with the proportions of both players and goal. We rather want a large goal being out of proportions, than a small goal with a tiny tap area. Around the field (sidelines and beside the goal) we would like advertising banners like seen on a real stadium.

The players
As mentioned we want 11 players in a 4-3-3 formation. The players should be attached to the board with springs as seen on some of the very old board games, where you could flick the player to pass the ball. This also means that we want the players to be placed in an indentation for the ball to fall into and it would be very cool if you could illustrate the player with the ball, as being pulled back to one of the sides, just enough to see the ball at his feet. The players should be large enough for a user to tap them, hence it would also be beneficial if they are not overlapping. For a start we would like to see the players in a blue shirt and white shorts (socks are not necessary as they are placed on a spring).

Scoreboard
On the scoreboard above the field, we need information such as the names of the two teams (could be FC Brightmoor and Tall Oak Rovers), the score (2-1), minutes played (42), and which half (1st). We also want a progress bar that illustrates how many moves you have used ranging from 0-5. The scoreboard could be inspired from the ones seen around stadiums across the world, but feel free to improvise.

What We Are Looking for
We are looking for full PSD and AI files so we can use them to make minor changes like colors on shirts and shorts, colors on pitch, etc. We really want you to be innovative and inspire us, as we are not designers ourselves. In the attached files, we have tried to sketch out a design that covers our initial ideas. We are looking for a professional look, and having the players and field look like a real board game would just be awesome. A combination of the look from the realistic pitch with advertising banners around it, the idea of our spring-players and the initial thoughts of a design illustrated in our sketch, should help you along. Flat design, cartoonish or somewhere in between is up to you, we just want you to impress and make "wow"-feeling.

QUESTION:
The final screen should display a question with four possible answers. There should be a green/checkmark when correct answer, and a red/cross if incorrect.

That's all. We are looking very much forward to see your designs!
Updates

Hi all,

We have changed the terms of the contest to now have a guaranteed payment, and we are really looking forward to see your designs! Good luck.

/ Mikkel and Anders

By request we have now uploaded an AI-file with the logo for you to play around with. We are looking forward to see your designs.

/ Mikkel and Anders

Reason: Hi designers, We are really happy with the progress being made, and are looking forward to see some of the designs that are still work in progress. However the amount of designs received, has not reached our expectations yet. Therefore we are extending the deadline for seven more days, so designers, that are still working on their designs can continue their work without a stressing deadline in the horizon. Good luck to all of you. We are looking very much forward to see, what you are able to produce. Best regards, Mikkel and Anders

Reason: Hi all, We still have a lot of designers in the competition , who are battling to finish their designs, therefore we have decided to extend the deadline once more. Good luck to all of you!

Target Market(s)

Football (soccer) fans

Industry/Entity Type

Advertising

```html
<!DOCTYPE html>
<html lang="en">
<head>
<meta charset="utf-8">
<title>Football Trivia – Home</title>
<link rel="stylesheet" href="https://fonts.googleapis.com/css2?family=Roboto:wght@300;400;700&display=swap">
<style>
  :root {
    --page-bg: #ececec;
    --status-bg: #1b1b1b;
    --header-bg: #1f1f1f;
    --pill-bg: #2c2c2c;
    --tab-bg-top: #545454;
    --tab-bg-bottom: #434343;
    --tab-rule: #9a9a9a;
    --section-bg: #393939;
    --quickplay-bg: #424242;
    --divider: #2a2a2a;
    --row-bg: #f3f3f3;
    --row-text: #555555;
    --white: #ffffff;
    --muted: #d6d6d6;
    --beat-red: #e0352b;
    --buy-green: #5e9a2c;
    --panel-dark: #2a2622;
    --panel-mid: #4a4038;
    --locked-light: #f3ece0;
    --locked-warm: #e8d9c0;
  }
  * { box-sizing: border-box; margin: 0; padding: 0; }
  html, body {
    width: 1200px; height: 1000px; overflow: hidden;
    background: var(--page-bg);
    font-family: "Roboto", "Helvetica Neue", Arial, sans-serif;
  }
  .stage {
    width: 1200px; height: 1000px;
    display: flex; align-items: center; justify-content: center;
  }
  .screen {
    width: 390px; height: 697px;
    background: var(--header-bg);
    overflow: hidden;
    position: relative;
    transform: scale(1.36);
    box-shadow: 0 2px 8px rgba(0,0,0,.15);
  }
  .status-bar {
    height: 22px; background: var(--status-bg); color: var(--white);
    display: flex; align-items: center; justify-content: space-between;
    padding: 0 8px; font-size: 13px; font-weight: 700; position: relative;
  }
  .status-bar .clock { position: absolute; left: 0; right: 0; text-align: center; }
  .signal { display: flex; gap: 2px; align-items: center; }
  .signal i { width: 6px; height: 6px; background: var(--white); border-radius: 50%; display: block; }
  .battery { width: 26px; height: 11px; border: 1px solid var(--white); border-radius: 2px; padding: 1px; }
  .battery span { display: block; height: 100%; background: var(--white); }

  .app-header {
    height: 56px; display: flex; align-items: center; justify-content: space-between;
    padding: 0 12px; position: relative; color: var(--white);
  }
  .settings-button {
    width: 31px; height: 31px; border: 1.5px solid var(--muted); border-radius: 50%;
    display: flex; align-items: center; justify-content: center;
  }
  .app-title { position: absolute; left: 0; right: 0; text-align: center; font-size: 20px; font-weight: 400; pointer-events: none; }
  .wins-pill {
    background: var(--pill-bg); color: var(--muted); font-size: 12px; font-weight: 400;
    padding: 9px 11px; border-radius: 16px; margin-right: -8px;
  }

  .tab-bar {
    height: 56px; display: flex; align-items: center;
    background: linear-gradient(var(--tab-bg-top), var(--tab-bg-bottom));
    border-bottom: 3px solid var(--tab-rule); position: relative;
  }
  .tab { color: var(--muted); font-size: 14.5px; text-align: center; position: relative; }
  .tab.home { width: 100px; color: var(--white); font-weight: 700; }
  .tab.games { width: 94px; }
  .tab.categories { width: 100px; }
  .tab.rankings { width: 90px; }
  .tab.home::after {
    content: ""; position: absolute; left: 50%; bottom: -26px; margin-left: -5px;
    border: 5px solid transparent; border-bottom-color: var(--tab-rule);
  }

  .section-title {
    height: 53px; background: var(--section-bg); color: var(--muted);
    font-size: 20px; font-weight: 300; display: flex; align-items: center; padding-left: 16px;
    border-bottom: 2px solid var(--divider);
  }
  .quick-play {
    height: 70px; background: var(--quickplay-bg); color: var(--white);
    font-size: 18px; font-weight: 700; display: flex; align-items: center; justify-content: center;
    border-bottom: 1px solid var(--divider);
  }

  .category-art { height: 102px; position: relative; }
  .category-art.stadium {
    background: linear-gradient(#9aa0a3 0%, #c9cdcd 14%, #56702f 20%, #4a6a24 55%, #3b5a1c 100%);
  }
  .category-art.fire {
    background: radial-gradient(ellipse at 28% 55%, #f1e6d4 0%, #e6882e 28%, #b5321a 48%, #1a0c08 72%),
                linear-gradient(90deg, #1a0c08, #3a1a10 60%, #0f2a20);
  }
  .scroll-thumb { position: absolute; right: 3px; top: 4px; width: 3px; height: 78px; background: rgba(255,255,255,.55); border-radius: 2px; }

  .category-row {
    height: 48px; background: var(--row-bg); color: var(--row-text);
    display: flex; align-items: center; justify-content: space-between;
    padding: 0 12px; font-size: 15px; font-weight: 300;
  }
  .category-row.locked { background: linear-gradient(90deg, var(--locked-light), var(--locked-warm)); color: #333; }
  .category-row small { font-size: 11px; }
  .chevron-circle { width: 25px; height: 25px; }

  .unlock-panel {
    height: 104px; position: relative; display: flex; align-items: center; padding: 0 20px;
    background: radial-gradient(ellipse at 45% 40%, var(--panel-mid), var(--panel-dark) 70%);
  }
  .unlock-option { display: flex; align-items: center; gap: 9px; color: var(--white); font-size: 12px; width: 175px; }
  .unlock-icon { width: 40px; height: 40px; border-radius: 50%; display: flex; align-items: center; justify-content: center; }
  .unlock-icon.beat { background: var(--beat-red); }
  .unlock-icon.buy { background: var(--buy-green); }
  .close-button { position: absolute; top: 8px; right: 5px; width: 19px; height: 19px; }
</style>
</head>
<body>
<div class="stage">
  <div class="screen">
    <div class="status-bar">
      <div class="signal"><i></i><i></i><i></i><i></i><i></i>
        <svg width="16" height="12" viewBox="0 0 16 12"><path d="M1 4a10 10 0 0 1 14 0M3.5 6.5a6.5 6.5 0 0 1 9 0M6 9a3 3 0 0 1 4 0" stroke="#fff" stroke-width="1.8" fill="none"/></svg>
      </div>
      <span class="clock">9:00 AM</span>
      <div class="battery"><span></span></div>
    </div>

    <header class="app-header">
      <div class="settings-button">
        <svg width="17" height="17" viewBox="0 0 24 24"><path fill="#e0e0e0" d="M10 1h4l.6 3 2.3 1 2.6-1.7 2.8 2.8L20.6 8.7l1 2.3 3 .6v4l-3 .6-1 2.3 1.7 2.6-2.8 2.8-2.6-1.7-2.3 1-.6 3h-4l-.6-3-2.3-1-2.6 1.7-2.8-2.8 1.7-2.6-1-2.3-3-.6v-4l3-.6 1-2.3L1.7 6.1l2.8-2.8 2.6 1.7 2.3-1zM12 8a4 4 0 1 0 0 8 4 4 0 0 0 0-8z" transform="translate(-.6 -.6) scale(1.05)"/></svg>
      </div>
      <h1 class="app-title">Title</h1>
      <span class="wins-pill">137 won matches</span>
    </header>

    <nav class="tab-bar">
      <span class="tab home">Home</span>
      <span class="tab games">My Games</span>
      <span class="tab categories">My Categories</span>
      <span class="tab rankings">Rankings</span>
    </nav>

    <h2 class="section-title">Choose Games Categories</h2>
    <div class="quick-play">Quick Play</div>

    <div class="category-art stadium" role="img" aria-label="Empty stadium with green grass pitch"><span class="scroll-thumb"></span></div>
    <div class="category-row">
      <span>Feature Categories</span>
      <svg class="chevron-circle" viewBox="0 0 26 26"><circle cx="13" cy="13" r="12" fill="none" stroke="#555" stroke-width="1.2"/><path d="M11 8l5 5-5 5" fill="none" stroke="#555" stroke-width="1.4"/></svg>
    </div>

    <div class="unlock-panel">
      <div class="unlock-option">
        <span class="unlock-icon beat"><svg width="20" height="22" viewBox="0 0 20 22"><path d="M6 10V5a1.5 1.5 0 0 1 3 0v4V3a1.5 1.5 0 0 1 3 0v6-4a1.5 1.5 0 0 1 3 0v8c0 4-2 7-6 7s-5-3-6-5l-1-3a1.5 1.5 0 0 1 3-1z" fill="#fff"/></svg></span>
        Beat to Unlock
      </div>
      <div class="unlock-option">
        <span class="unlock-icon buy"><svg width="20" height="18" viewBox="0 0 20 18"><path d="M1 2h3l2 9h10l2-7H5" fill="none" stroke="#fff" stroke-width="1.8"/><circle cx="7.5" cy="15" r="1.6" fill="#fff"/><circle cx="14.5" cy="15" r="1.6" fill="#fff"/></svg></span>
        Buy to Unlock
      </div>
      <svg class="close-button" viewBox="0 0 20 20"><circle cx="10" cy="10" r="9.5" fill="#fff"/><path d="M6.5 6.5l7 7M13.5 6.5l-7 7" stroke="#222" stroke-width="2.2"/></svg>
    </div>
    <div class="category-row locked">
      <span>Feature Categories <small>(Locked)</small></span>
      <svg class="chevron-circle" viewBox="0 0 26 26"><circle cx="13" cy="13" r="12" fill="none" stroke="#777" stroke-width="1.2"/><path d="M8 15l5-5 5 5" fill="none" stroke="#777" stroke-width="1.4"/></svg>
    </div>

    <div class="category-art fire" role="img" aria-label="Football wrapped in flames"></div>
    <div class="category-row">
      <span>Feature Categories</span>
      <svg class="chevron-circle" viewBox="0 0 26 26"><circle cx="13" cy="13" r="12" fill="none" stroke="#555" stroke-width="1.2"/><path d="M11 8l5 5-5 5" fill="none" stroke="#555" stroke-width="1.4"/></svg>
    </div>
  </div>
</div>
</body>
</html>
```